Poster Design - Stand Up Paddle Eco Tour

We need a A3 size poster design (using Adobe Illustrator) for our company's stand up paddle tour. Our tour is on flat water, calm and safe, suitable for all ages and level.

WE provide worldclass SUP boards for our customers. And branded Joren Maltby life jacket. Our instructors are all well trained and exeprience. Plus they are super friendly. Every paddling trip come with a safety boat.

Please refer to attached files for text and photos.

Our website is www.brinkwaveoar.com.sg

IMPORTANT NOTE - The design has to be done in Adobe Illustrator. The winning designer has to submit the working file in Adobe Illustrator.

Target Market(s)

Working adult - 20 - 35 year old

Industry/Entity Type

Tourism

Requirements
Must have
• The project MUST be done in Adobe Illustrator and the winning designer has to submit the artwork to us in Adobe Illustrator format.
Nice to have
• pleasant to look at.

```html
<!DOCTYPE html>
<html lang="en">
<head>
<meta charset="utf-8">
<title>Brink Wave Oar – SUP &amp; Eco Tour Poster</title>
<link rel="stylesheet" href="https://fonts.googleapis.com/css2?family=PT+Sans+Narrow:wght@400;700&family=Source+Sans+3:wght@400;600&display=swap">
<style>
  :root{
    --sky:#e9edf0;
    --mist:#b9c7d1;
    --mangrove:#2e5a78;
    --mangrove-deep:#1c3d57;
    --orange:#f39a3a;
    --band:rgba(214,160,82,.82);
    --navy:#1d3048;
    --white:#ffffff;
    --water:#5fa59a;
    --water-blue:#4d94b4;
  }
  *{margin:0;padding:0;box-sizing:border-box}
  html,body{width:852px;height:1200px;overflow:hidden;background:#fff}
  .poster{position:relative;width:852px;height:1200px;overflow:hidden;
    font-family:"Source Sans 3",Arial,sans-serif;color:var(--white)}
  .backdrop{position:absolute;inset:0;
    background:linear-gradient(180deg,var(--sky) 0%,#dde4ea 16%,var(--mist) 30%,#5e819b 44%,var(--mangrove) 58%,var(--mangrove-deep) 85%,#243f54 100%)}
  .photo-frame{position:absolute;left:443px;top:0;width:372px;height:1072px;background:var(--white)}
  .photo{position:absolute;left:455px;width:348px}
  .photo--river{top:0;height:221px;background:linear-gradient(180deg,#cfe3ef 0%,#3f7a3a 30%,#4f8a4a 50%,var(--water) 75%,#6aa08e 100%)}
  .photo--group{top:244px;height:260px;background:linear-gradient(180deg,#a9cde8 0%,#dbeaf4 35%,var(--water-blue) 50%,#3f86a0 100%)}
  .photo--mangrove{top:527px;height:260px;background:linear-gradient(180deg,#cfe3ef 0%,#2f6a39 25%,#3c7a45 45%,#3f8a7c 65%,#4b8f86 100%)}
  .photo--bay{top:810px;height:260px;background:linear-gradient(180deg,#8fc0e4 0%,#d9eaf5 45%,#7fb8d4 60%,#5aa3c0 100%)}
  .brand{position:absolute;left:26px;top:62px;display:flex;align-items:center;gap:8px;
    color:var(--navy);font-family:"PT Sans Narrow",Arial,sans-serif;font-weight:700;font-size:24px}
  .brand-dot{width:14px;height:14px;border-radius:50%;background:var(--navy)}
  .headline{position:absolute;left:26px;top:276px;color:#111;font-family:"PT Sans Narrow",Arial,sans-serif}
  .headline-lead{font-size:50px;line-height:52px;font-weight:400}
  .headline-sub{font-size:30px;line-height:33px;font-weight:400}
  .headline-product{position:absolute;left:26px;top:404px;white-space:nowrap;
    font-family:"PT Sans Narrow",Arial,sans-serif;font-weight:700;font-size:48px;color:var(--orange);opacity:.92}
  .intro{position:absolute;left:26px;top:572px;font-family:"PT Sans Narrow",Arial,sans-serif;font-size:16px;line-height:21px}
  .callout{color:var(--orange);font-family:"PT Sans Narrow",Arial,sans-serif;font-weight:700}
  .intro .callout{font-size:26px;margin-top:8px}
  .guided{position:absolute;left:26px;top:782px;width:360px}
  .guided h2{font-size:26px;line-height:24px;margin-bottom:10px;font-family:"Source Sans 3",Arial,sans-serif;font-weight:600;color:var(--orange)}
  .guided p{font-size:15px;line-height:21px}
  .info-band{position:absolute;left:0;top:1010px;width:852px;height:190px;background:var(--band)}
  .info{position:absolute;color:var(--white);font-size:14px;line-height:18px}
  .info h3{font-size:20px;font-weight:600;color:var(--navy);line-height:22px}
  .info--timing{left:26px;top:1033px}
  .info--location{left:26px;top:1087px}
  .booking{position:absolute;left:423px;top:1031px}
  .booking h3{font-size:22px;font-weight:600;color:var(--navy)}
  .booking .note{font-size:16px;color:var(--navy);margin:2px 0 4px}
  .booking ul{list-style:none;font-size:14px;line-height:21px;color:var(--white)}
  .booking li{display:flex;align-items:center;gap:12px;padding-left:12px}
  .booking li::before{content:"";width:7px;height:7px;border-radius:50%;background:#ffb43a}
</style>
</head>
<body>
<main class="poster">
  <div class="backdrop" role="img" aria-label="Duotone photo of a paddler standing on a board among mangrove trees under a cloudy sky"></div>

  <div class="photo-frame"></div>
  <div class="photo photo--river" role="img" aria-label="Paddlers on a calm river lined with mangroves"></div>
  <div class="photo photo--group" role="img" aria-label="Group of paddlers on boards in open water near a jetty"></div>
  <div class="photo photo--mangrove" role="img" aria-label="Two paddlers on yellow boards in front of mangrove forest"></div>
  <div class="photo photo--bay" role="img" aria-label="Paddlers spread across a wide bay under blue sky"></div>

  <div class="brand"><span class="brand-dot"></span>Brink Wave Oar</div>

  <div class="headline">
    <div class="headline-lead">Explore</div>
    <div class="headline-sub">the natural coastal surroundings<br>and waterways of Johor on a</div>
  </div>
  <div class="headline-product">SUP Adventure Touring Board</div>

  <div class="intro">
    <p>Our tours are flat-water and appropriate for all ages and levels.<br>We have the best possible service and equipment.</p>
    <p class="callout">Join us for a fun and relaxing day</p>
  </div>

  <section class="guided">
    <h2>What could be better than<br>a group guided tour?</h2>
    <p>With life vests and a safety boat for our guided tour, you can be assured of a secured environment while you focus on just having fun and creating life’s best memories with friends and family.</p>
  </section>

  <div class="info-band"></div>
  <div class="info info--timing">
    <h3>Timing</h3>
    <p>Morning, afternoon, and sunset session</p>
  </div>
  <div class="info info--location">
    <h3>Location</h3>
    <p>Selat Tenang River, set off from Teluk Damar,<br>Pantai Sejuk. (next to Pasir Lembut)</p>
  </div>

  <div class="booking">
    <h3>Contact us for booking</h3>
    <p class="note">We do not accept walk-in</p>
    <ul>
      <li>+65-6000-2417</li>
      <li>www.brinkwaveoar.com.sg</li>
      <li>social: @brinkwaveoar</li>
      <li>booking@brinkwaveoar.com.sg</li>
    </ul>
  </div>
</main>
</body>
</html>
```